Design for NFT project with multiple collections

We need a website for an NFT project that will allow purchasing NFTs in an initial collection, as well as providing information on the overall project and the roadmap of all the collections to come in the future.
Logo is provided as well as an image that we'd like to be "worked in" as best as possible but this is not required. If different versions of the site are required please let me know.
General Guidelines:
- responsive website (with tailwindcss if possible)
- Dark theme only
- Place logo top left
- normal text white
- headings "yellow" or "red"
- no preference on font
- include discord, twitter and IG icons somewhere
- include a countdown somewhere that will go after launch
- home page will display buying option (see example #1)
- home page will also display 6 characters with description (see example #2)
Example/Guide Sites:
#1. https://www.vorendaleguild.example
#2. https://tinycometcrew.example
#3. https://www.marbleowlcollectivenft.example

```html
<!DOCTYPE html>
<html lang="en">
<head>
<meta charset="utf-8">
<title>Hayloft Ruckus — NFT Collection</title>
<link rel="stylesheet" href="https://fonts.googleapis.com/css2?family=Oranienbaum&family=Work+Sans:wght@400;500;600&display=swap">
<style>
:root{
  --bg:#f2f2f2;
  --ink:#000;
  --white:#fff;
  --yellow:#f6e61c;
  --red:#b3121b;
  --teal:#4b8b9b;
  --teal-line:#3f8f8c;
  --panel-a:#3d5a63;
  --panel-b:#22393f;
  --wood:#c98a4e;
  --wood-dark:#8a5a2b;
  --gold:#b48a3c;
  --muted:#bdbdbd;
  --display:'Oranienbaum',serif;
  --body:'Work Sans',sans-serif;
}
*{margin:0;padding:0;box-sizing:border-box}
html,body{width:1200px;height:3380px;overflow:hidden;background:var(--bg)}
body{font-family:var(--body);color:var(--white);position:relative}
.page{position:absolute;left:148px;top:53px;width:906px;height:3282px;background:var(--ink);overflow:hidden}
.abs{position:absolute}

/* hero */
.hero-art{left:0;top:0;width:906px;height:552px;
  background:linear-gradient(180deg,#2b2e34 0%,#3a3c40 35%,#3a3f2c 60%,#2d4a1f 82%,#1f3514 100%)}
.nav{left:0;top:0;width:906px;height:56px;display:flex;align-items:center;padding:0 68px;
  background:linear-gradient(180deg,rgba(0,0,0,.55),rgba(0,0,0,0))}
.brand{font-family:var(--display);font-size:22px;color:var(--yellow);display:flex;align-items:center;gap:8px;line-height:1}
.brand .dot{width:14px;height:14px;border-radius:50%;background:var(--yellow)}
.nav ul{margin-left:auto;display:flex;gap:20px;list-style:none;font-size:9px;align-items:center}
.wallet{background:#1a0608;border:1px solid var(--red);padding:8px 10px;font-size:8px;letter-spacing:.4px;text-transform:uppercase}

/* countdown */
.countdown{left:68px;top:473px;width:768px;height:224px;border:2px solid var(--gold);border-radius:12px;
  background:linear-gradient(180deg,rgba(70,70,60,.85),rgba(40,40,35,.9))}
.countdown h2{font-family:var(--display);font-weight:400;font-size:28px;position:absolute;left:28px;top:12px;line-height:1.2}
.cells{position:absolute;left:0;right:0;top:62px;bottom:0;display:grid;grid-template-columns:repeat(4,1fr)}
.cell{border:2px solid var(--gold);border-radius:12px;text-align:center;background:linear-gradient(180deg,#4a4638,#2b2a25);padding-top:30px}
.cell b{display:block;font-family:var(--display);font-weight:400;font-size:58px;line-height:1}
.cell span{font-family:var(--display);font-size:22px;color:var(--yellow)}

/* about */
.always{left:68px;top:806px;font-family:var(--display);color:var(--yellow);font-size:50px;line-height:52px}
.always .row{display:block;height:54px;white-space:nowrap}
.always .cap{font-size:118px;line-height:0;vertical-align:-2px}
.about{left:388px;top:746px;width:440px}
.about .eyebrow{font-size:12px}
.about h3{font-family:var(--display);font-weight:400;font-size:22px;letter-spacing:1px;margin:18px 0 20px;line-height:1.3;text-transform:uppercase}
.about h3 em{font-style:normal;color:var(--yellow)}
.about p{font-size:10.5px;line-height:1.8}

/* collection */
.collection{left:0;width:906px;top:1060px;text-align:center}
.collection .count{font-family:var(--display);font-size:34px;line-height:1.1}
.collection h2{font-family:var(--display);font-weight:400;color:var(--teal);font-size:40px;line-height:1.1}
.collection p{font-size:10.5px;line-height:1.5;margin-top:8px}
.bid-box{left:177px;top:1248px;width:545px;height:526px;border:2px solid var(--teal-line);border-radius:12px}
.bid-head{position:absolute;left:30px;right:30px;top:18px;display:flex;justify-content:space-between;font-size:10.5px;color:var(--yellow);line-height:1.4}
.bid-head .right{text-align:center}
.bid-foot{position:absolute;bottom:10px;left:0;right:0;text-align:center;font-family:var(--display)}
.bid-foot b{font-weight:400;font-size:30px;display:block;line-height:1}
.bid-foot span{color:var(--teal);font-size:28px}
.bid-grid{left:141px;top:1303px;width:608px;height:380px;border:12px solid var(--wood);outline:2px solid var(--wood-dark);
  display:grid;grid-template-columns:1fr 1fr;grid-template-rows:1fr 1fr;background:var(--wood)}
.tile{display:flex;align-items:center;justify-content:center;font-family:var(--display);font-size:32px;margin:2px}
.tile.a{background:var(--panel-a)}.tile.b{background:var(--panel-b)}
.current{flex-direction:column;align-items:flex-start;padding-left:84px;line-height:1.1}
.current small{font-family:var(--body);font-size:10px;color:var(--yellow)}
.current em{font-style:normal;font-family:var(--body);font-size:14px}
.tokens{gap:40px;font-size:24px;text-align:center;line-height:1.3}
.tokens div+div{border-left:1px solid #6c8890;padding-left:40px}
.sold{flex-direction:column;gap:6px}
.note{left:0;width:906px;top:1791px;text-align:center;font-size:10.5px;line-height:1.6}
.btn{top:1872px;height:28px;font-size:8px;text-transform:uppercase;display:flex;align-items:center;justify-content:center;letter-spacing:.4px}
.btn.place{left:344px;width:95px;background:linear-gradient(90deg,#3a0507,var(--red))}
.btn.view{left:464px;width:98px;border:1.5px solid var(--white);background:#111}

/* characters */
.char{width:206px;text-align:center}
.frame{width:206px;height:200px;border:12px solid var(--wood);outline:2px solid var(--wood-dark);
  background:radial-gradient(circle,#6a2a26 0%,#4b4036 65%)}
.char small{display:block;font-size:10px;margin-top:28px}
.char h4{font-family:var(--display);font-weight:400;font-size:32px;line-height:1.2;margin-top:8px}
.char span{font-family:var(--display);color:var(--yellow);font-size:28px}

/* footer */
.footer-art{left:0;top:2920px;width:906px;height:362px;
  background:linear-gradient(180deg,#000 0%,#0f1c0b 30%,#1e3515 70%,#24401a 100%)}
.foot-brand{left:68px;top:2838px}
.socials{left:68px;top:2872px;display:flex;gap:6px}
.socials span{width:20px;height:20px;border:1.5px solid var(--white);border-radius:50%}
.rights{left:68px;top:2901px;font-size:8px;color:var(--muted)}
.policy{left:301px;top:2840px}
.policy h5{font-size:12px;font-weight:600}
.policy p{font-size:8px;color:var(--muted);margin-top:10px}
</style>
</head>
<body>
<main class="page">
  <div class="abs hero-art" role="img" aria-label="Night farm illustration: moonlit barn with glowing green doorway, windmill, hay bale and a hooded mascot"></div>
  <header class="abs nav">
    <div class="brand"><span class="dot"></span>Hayloft Ruckus</div>
    <ul><li>About</li><li>Roadmap</li><li>FAQs</li><li>Team</li><li class="wallet">Wallet Connect</li></ul>
  </header>

  <section class="abs countdown">
    <h2>Auction Ends in</h2>
    <div class="cells">
      <div class="cell"><b>00</b><span>Days</span></div>
      <div class="cell"><b>00</b><span>Hours</span></div>
      <div class="cell"><b>00</b><span>Minutes</span></div>
      <div class="cell"><b>00</b><span>Seconds</span></div>
    </div>
  </section>

  <div class="abs always"><span class="row"><span class="cap">A</span>lways</span><span class="row"><span class="cap">A</span>uthentic</span></div>
  <section class="abs about">
    <div class="eyebrow">About Us</div>
    <h3>A <em>Hayloft Ruckus</em> that actually has a world to play in</h3>
    <p>When we created the Lanternway world, we always believed in building the world first before filling it with inhabitants. With the world drawing ever closer to launch, we wanted to offer the chance to enter our world alongside 7,500 unique (character name here) on the Corvane blockchain, designed to have utility in our metaverse immediately. To get started please complete this Glint Challenge to get whitelisted!</p>
  </section>

  <section class="abs collection">
    <div class="count">1000<small style="font-size:14px">+</small></div>
    <h2>Randomly<br>Generated (Character name here)</h2>
    <p>Connect your wallet and generate your own<br>randomized bulls.</p>
  </section>

  <div class="abs bid-box">
    <div class="bid-head">
      <div>Early Access: October 15th 2021, 06:00 AM EST<br>Full Access: October 15th 2021, 06:00 PM EST</div>
      <div class="right">Unlock 16 Hours<br>Early by Holding</div>
    </div>
    <div class="bid-foot"><b>100<small style="font-size:14px">+</small></b><span>Unique Bulls</span></div>
  </div>
  <div class="abs bid-grid">
    <div class="tile a current"><small>Current Bid</small>3.00 ETH<em>$9000.00</em></div>
    <div class="tile b tokens"><div>1,000<br>BITT</div><div>10<br>CGG</div></div>
    <div class="tile b sold">
      <svg width="30" height="30" viewBox="0 0 30 30" aria-hidden="true"><circle cx="15" cy="15" r="13" fill="none" stroke="#fff" stroke-width="2"/><path d="M12 9l6 6-6 6" fill="none" stroke="#fff" stroke-width="2"/></svg>
      Sold Out</div>
    <div class="tile a">00 NFT</div>
  </div>

  <p class="abs note">Connect your wallet and generate your own randomized bulls.<br>Our minting process selects from 7 random Traits giving a Possibility<br>of over 294 billion unique options.</p>
  <div class="abs btn place">Place Bid</div>
  <div class="abs btn view">View Artwork</div>

  <article class="abs char" style="left:68px;top:1983px"><div class="frame" role="img" aria-label="Red bull character artwork"></div><small>Prototype</small><h4>Bulls</h4><span>#0001</span></article>
  <article class="abs char" style="left:349px;top:1983px"><div class="frame" role="img" aria-label="Red bull character artwork"></div><small>Prototype</small><h4>Bulls</h4><span>#0002</span></article>
  <article class="abs char" style="left:630px;top:1983px"><div class="frame" role="img" aria-label="Red bull character artwork"></div><small>Prototype</small><h4>Bulls</h4><span>#0003</span></article>
  <article class="abs char" style="left:68px;top:2371px"><div class="frame" role="img" aria-label="Red bull character artwork"></div><small>Prototype</small><h4>Bulls</h4><span>#0004</span></article>
  <article class="abs char" style="left:349px;top:2371px"><div class="frame" role="img" aria-label="Red bull character artwork"></div><small>Prototype</small><h4>Bulls</h4><span>#0005</span></article>
  <article class="abs char" style="left:630px;top:2371px"><div class="frame" role="img" aria-label="Red bull character artwork"></div><small>Prototype</small><h4>Bulls</h4><span>#0006</span></article>

  <div class="abs footer-art" role="img" aria-label="Illustration of an angry horned cow mascot lying with a yellow pitchfork on dark grass"></div>
  <div class="abs brand foot-brand"><span class="dot"></span>Hayloft Ruckus</div>
  <div class="abs socials" aria-label="Social links"><span></span><span></span><span></span><span></span><span></span></div>
  <div class="abs rights">2021, All rights reserved by NIGHTHARE.</div>
  <div class="abs policy"><h5>Policy ID</h5><p>hrx0a91k2mqv7tz4pdl8wec3ufy0001</p></div>
</main>
</body>
</html>
```